Foremost expert on sales tools need a slider graphic for top of home page

I'm having a new website designed. And I have the need for lots of graphics.
Ultimately, I will need 3 graphics created for our home page. But I'd like to start with ONE that will compel people to subscribe to our newsletter.

It's a B2B site, so it needs to be business-like. On the other-hand, I want it to have an emotional connection (in other words, no std business people silhouettes). The banner should have some text that describes the fact that 30,000 sales professionals subscribe to our weekly newsletter (the message is: you will be in good company). So why not take the plunge.

You can see our homepage rough draft mock-up here. The slider you see is the Wordpress standard slider. Yours will REPLACE this place-holder slider. http://brenvoxa.net/qqdemo

You can see our current site here: www.keenpitchkit.net in case it helps to understand more about our business.

This is my first time using ArtHarbor. I have marked the budget as refundable because I don't know what to expect. My desire is to select a winning design, which I desperately need - not to get a refund.

Industry/Entity Type

Business

Requirements
Must have
• The slider should contain a button for people to click on that will take them to a subscribe page.

```html
<!DOCTYPE html>
<html lang="en">
<head>
<meta charset="utf-8">
<title>Keen Pitch Kit – Home</title>
<link rel="stylesheet" href="https://fonts.googleapis.com/css2?family=Antic+Slab&family=Noto+Serif&family=PT+Sans+Narrow&family=Open+Sans:wght@400&display=swap">
<style>
  :root {
    --brand-blue: #0b9fd9;
    --ink: #333333;
    --muted: #6b6b6b;
    --rule: #e2e2e2;
    --cta-top: #eef27a;
    --cta-bottom: #d3dc36;
    --sub-text: #c9f1ff;
    --white: #ffffff;
  }
  * { box-sizing: border-box; margin: 0; padding: 0; }
  html, body { width: 1200px; height: 779px; overflow: hidden; background: var(--white); }
  body { position: relative; font-family: "Antic Slab", Georgia, serif; color: var(--ink); }

  .topbar { position: absolute; left: 0; top: 0; width: 1200px; height: 42px; background: var(--brand-blue); }
  .social { position: absolute; left: 176px; top: 13px; display: flex; gap: 18px; list-style: none; }
  .social li { width: 15px; height: 15px; border-radius: 50%; background: #5cc4ea; }
  .utility-nav { position: absolute; right: 168px; top: 14px; display: flex; list-style: none; font-family: "Open Sans", Arial, sans-serif; font-size: 10px; color: var(--white); }
  .utility-nav li { padding: 0 9px; border-left: 1px solid rgba(255,255,255,.8); line-height: 12px; }
  .utility-nav li:first-child { border-left: 0; }
  .utility-nav li:last-child { padding-right: 0; }

  .masthead { position: absolute; left: 0; top: 42px; width: 1200px; height: 147px; border-bottom: 1px solid var(--rule); }
  .brand-name { position: absolute; left: 177px; top: 58px; font-family: "Antic Slab", Georgia, serif; font-size: 24px; line-height: 30px; color: var(--ink); white-space: nowrap; }
  .tagline { position: absolute; left: 360px; top: 38px; width: 464px; text-align: center; font-size: 18px; line-height: 27px; color: #3a3a3a; }
  .tagline strong { font-weight: 400; font-size: 18px; display: block; color: #2a2a2a; text-shadow: 0 0 .4px #2a2a2a; }
  .search { position: absolute; left: 838px; top: 43px; width: 200px; height: 25px; border: 1px solid var(--rule); font-family: "Open Sans", Arial, sans-serif; font-size: 11px; color: #b5b5b5; padding: 5px 6px; }

  .main-nav { position: absolute; left: 177px; top: 189px; height: 41px; display: flex; gap: 32px; list-style: none; font-size: 13px; line-height: 41px; color: #444; }
  .main-nav .current { color: var(--brand-blue); }

  .hero { position: absolute; left: 0; top: 230px; width: 1200px; height: 399px; overflow: hidden;
          background: radial-gradient(ellipse at 40% 40%, #2fb6e8 0%, #14a4dd 45%, #0a97d5 100%);
          box-shadow: inset 0 6px 8px -6px rgba(0,0,0,.35); }
  .hero-decor { position: absolute; left: 0; top: 0; }
  .hero-copy { position: absolute; left: 253px; top: 54px; color: var(--white); font-family: "Noto Serif", Georgia, serif; text-shadow: 0 1px 2px rgba(0,40,80,.35); }
  .hero-join { font-size: 29px; line-height: 32px; }
  .hero-count { font-size: 72px; line-height: 78px; margin-top: -2px; }
  .hero-audience { font-size: 27px; line-height: 32px; margin-top: -2px; }
  .hero-offer { position: absolute; left: 253px; top: 213px; font-family: "PT Sans Narrow", Arial, sans-serif; font-size: 21px; line-height: 24px; color: var(--sub-text); }
  .subscribe-btn { position: absolute; left: 254px; top: 293px; width: 131px; height: 39px; background: linear-gradient(var(--cta-top), var(--cta-bottom));
                   font-family: "PT Sans Narrow", Arial, sans-serif; font-size: 20px; line-height: 39px; text-align: center; color: #3a3a2a; letter-spacing: .5px; text-decoration: none; }
  .team-photo { position: absolute; left: 647px; top: 24px; width: 325px; height: 375px;
                background: linear-gradient(180deg, #8a9199 0%, #5d646c 55%, #4a4f56 100%);
                border-radius: 150px 150px 40px 40px; opacity: .92; }

  .features { position: absolute; left: 177px; top: 681px; display: flex; }
  .feature { width: 294px; }
  .feature-head { display: flex; align-items: center; gap: 10px; }
  .feature-icon { width: 31px; height: 31px; border-radius: 50%; background: #2e2e2e; display: flex; align-items: center; justify-content: center; }
  .feature-title { font-family: "Antic Slab", Georgia, serif; font-weight: 400; font-size: 17px; color: #333; }
  .feature-text { margin-top: 13px; font-family: "Open Sans", Arial, sans-serif; font-size: 11px; line-height: 19px; color: var(--muted); width: 270px; }
</style>
</head>
<body>
  <header class="topbar">
    <ul class="social" aria-label="Social links">
      <li></li><li></li><li></li><li></li><li></li><li></li><li></li>
    </ul>
    <ul class="utility-nav">
      <li>Home</li><li>About</li><li>Press</li>
    </ul>
  </header>

  <section class="masthead">
    <div class="brand-name">Keen Pitch Kit</div>
    <p class="tagline">Buyer Resources for Discovering, Assessing and Choosing<strong>The Best Sales and Marketing Software</strong></p>
    <div class="search">Search ...</div>
  </section>

  <ul class="main-nav">
    <li class="current">Home</li>
    <li>Subscribe</li>
    <li>Sales Solutions</li>
    <li>Buyer Resources</li>
    <li>Current News letter</li>
  </ul>

  <section class="hero">
    <svg class="hero-decor" width="1200" height="399" aria-hidden="true">
      <circle cx="899" cy="175" r="150" fill="#0a8ccc" opacity=".55"/>
      <circle cx="555" cy="210" r="130" fill="#ffffff" opacity=".05"/>
      <circle cx="290" cy="400" r="90" fill="#ffffff" opacity=".06"/>
      <circle cx="430" cy="354" r="17" fill="none" stroke="#7fd3f2" stroke-width="3" opacity=".55"/>
      <circle cx="957" cy="8" r="28" fill="none" stroke="#7fd3f2" stroke-width="3" opacity=".45"/>
      <circle cx="1000" cy="45" r="10" fill="none" stroke="#7fd3f2" stroke-width="2" opacity=".4"/>
    </svg>
    <div class="hero-copy">
      <div class="hero-join">Join</div>
      <div class="hero-count">30,000</div>
      <div class="hero-audience">Sales and Marketing Leaders</div>
    </div>
    <p class="hero-offer">FREE Information on Marketing &amp; Sales<br>Software and Sales Productivity Tools</p>
    <a class="subscribe-btn" href="#subscribe">SUBSCRIBE</a>
    <div class="team-photo" role="img" aria-label="Photo of a large group of smiling sales professionals in business suits standing together, viewed from above"></div>
  </section>

  <section class="features">
    <article class="feature">
      <div class="feature-head">
        <span class="feature-icon"><svg width="12" height="14" viewBox="0 0 12 14" aria-hidden="true"><rect x="1" y="1" width="10" height="12" rx="1.5" fill="none" stroke="#fff" stroke-width="1.6"/></svg></span>
        <h2 class="feature-title">Sales Solutions</h2>
      </div>
      <p class="feature-text">Find the best sales software tools to increase sales productivity and grow revenue.</p>
    </article>
    <article class="feature">
      <div class="feature-head">
        <span class="feature-icon"><svg width="16" height="14" viewBox="0 0 16 14" aria-hidden="true"><path d="M1 3h4l6 8h4M1 11h4l6-8h4M13 1l2 2-2 2M13 9l2 2-2 2" fill="none" stroke="#fff" stroke-width="1.6"/></svg></span>
        <h2 class="feature-title">Buyer Resources</h2>
      </div>
      <p class="feature-text">Download Buyer Guides, Self-Assessments, Buyer Check-Lists, and other informative resources.</p>
    </article>
    <article class="feature">
      <div class="feature-head">
        <span class="feature-icon"><svg width="10" height="14" viewBox="0 0 10 14" aria-hidden="true"><path d="M5 1C5 1 1 6 1 9a4 4 0 0 0 8 0C9 6 5 1 5 1z" fill="#fff"/></svg></span>
        <h2 class="feature-title">Weekly Events Resources</h2>
      </div>
      <p class="feature-text">View our most recent newsletter including our Recommended Tool of the Week.</p>
    </article>
  </section>
</body>
</html>
```